Brochure required for international Sports event

We need an 8 page brochure designed for an international sports event to be hosted in Japan. We are a Travel Company providing packages for participants looking to travel to the event.
The brochure will feature information on the event as well as services our company can provide.
The Brochure is to be an 8 page A4 document in portrait layout.
The brochure needs to be provided both as a print ready document and digital brochure for emailing.
Brochure structure, copy, logo and imagery has been provided
As well as a example brochure design that we like for inspiration.
Link to icons - https://www.filevault-example.net/sh/kq3mzplr8wbtyoc/BBBxkTLmQ4pR7Hs2nW6vYbCgE?dl=0
Target Market(s)
Masters/Veterans Sports Participants
Industry/Entity Type
Travel
Colors
Designer to choose colors to be used in the design.
Look and feel
Each slider illustrates characteristics of the customer's brand and the style your logo design should communicate.

```html
<!DOCTYPE html>
<html lang="en">
<head>
<meta charset="utf-8">
<title>Global Veterans Games – Kansai</title>
<link href="https://fonts.googleapis.com/css2?family=Jost:wght@400;500&display=swap" rel="stylesheet">
<style>
  :root {
    --brand-red: #e5262a;
    --text-light: #ffffff;
    --photo-sky: #dfe3e2;
    --photo-vest: #d7e83a;
    --photo-rail: #2f5a4c;
    --mascot-pink: #f4b6d8;
  }
  html, body {
    margin: 0;
    padding: 0;
    overflow: hidden;
  }
  body {
    width: 848px;
    height: 1200px;
    background: var(--brand-red);
    font-family: "Jost", "Futura", sans-serif;
    color: var(--text-light);
    position: relative;
  }
  .page-title {
    position: absolute;
    left: 52px;
    top: 52px;
    margin: 0;
    font-weight: 500;
    font-size: 54px;
    line-height: 1;
    letter-spacing: 0.3px;
  }
  .intro {
    position: absolute;
    left: 59px;
    top: 125px;
    width: 218px;
    font-size: 18px;
    line-height: 25.7px;
  }
  .intro p,
  .region-copy p {
    margin: 0 0 7px;
  }
  .hero-photo {
    position: absolute;
    left: 303px;
    top: 128px;
    width: 545px;
    height: 833px;
    background: linear-gradient(160deg, var(--photo-sky) 0%, #cfd6cf 40%, var(--photo-vest) 75%, var(--photo-rail) 100%);
  }
  .mascot {
    position: absolute;
    left: 118px;
    top: 728px;
    width: 102px;
    height: 154px;
    border-radius: 40px;
    background: radial-gradient(circle at 50% 40%, #fbd6ea, var(--mascot-pink));
  }
  .region-title {
    position: absolute;
    left: 52px;
    top: 916px;
    margin: 0;
    font-weight: 500;
    font-size: 52px;
    line-height: 1;
  }
  .region-copy {
    position: absolute;
    left: 51px;
    top: 978px;
    width: 750px;
    font-size: 18px;
    line-height: 25.5px;
  }
</style>
</head>
<body>
  <h1 class="page-title">The Global Veterans Games</h1>

  <section class="intro">
    <p>The 2021 Global Veterans Games will be the 10th Edition of the Games and the first time it will be held in Asia. Since its inception in Toronto in 1985 the Global Veterans Games has grown to become the world’s largest mass-participated international sports event.</p>
    <p>The 2021 Games will be held in the Kansai region in the west of Japan and will take place over 17 days from May 14 – 30. An estimated 50,000 participants will meet to play a total of 65 sports and explore this beautiful and alluring country.</p>
  </section>

  <div class="hero-photo" role="img" aria-label="Photo of a veteran runner in a yellow vest stretching his leg on a green railing"></div>

  <div class="mascot" role="img" aria-label="Pink fox-like event mascot character waving"></div>

  <h2 class="region-title">Kansai</h2>

  <section class="region-copy">
    <p>Kansai consists of seven prefectures and was formerly the political and cultural center of Japan for many centuries and includes the cities of Kyoto, Osaka, Nara and Kobe.</p>
    <p>The Kansai region is located in the center of the Japanese islands and is home to over 20 million people. The region is also host to a number of incredible sights including Osaka Castle, Fushimi Inari Shrine, Kinkaku-ji (the Golden Pavilion), Nara Deer Park, Dotonbori District Nishiki Markets and Arashiyama Bamboo Grove.</p>
  </section>
</body>
</html>
```